Web Design Project (Renewable Energy Services Company)

Hello crowd,

We are looking to create a website for a new company. We would like to have the page already coded, if you do not provide the code as well, please indicate so. I am including a very preliminary approximation of the wireframe.

We do not have the logo either the color pallet, however we have in mind couple websites that would be similar tho these.

http://www.brivolen.com/en/

and

http://www.tarmuvex.com/

We did an approximated wireframe our our website, not necesarly to decide on the layout but rather to know how many pages will be needed. It would be around 10 pages. We will need a section that will be an e-commerce page to sell products such as engineering instrumentation, software and consumables such as cable and connectors.

Our company will be called ORVIK. We will be based in Monterrey, Mexico. Our focused will be the development of renewable energy projects. Similar scope of services than http://www.brivolen.com/en/ but only for wind and solar projects.

We like something minimalistic. Some of the things that the logo might or might not include would be the monterrey famous hill, but not strictly necessary.
http://en.plavorinet.org/wiki/Loma_del_Trueno

also ORVIK (which stands for ORganica VIKtoria) the name is similar the bird (seagal) or wind turbines and sun...any of these are only suggestions and we are open to receive any proposals.

There must be a
home page
services page (some subsections)
products page (some subsections)
contact page with contact form

and some additional subsections like careers and partnerships.

We are very excited to start hearing about this project.
Updates

Please for the logo, do not restrict your ideas to the ones provided as it has generated too specific logos. Pleae just allow your imagination to flow for a company that develops renewable energy projects.

Target Market(s)

large companies interested in developing renewable energy projects

Industry/Entity Type

E-Commerce

Requirements
Must have
• Minimalistic and unique design.
Nice to have
• contact form to save contacts in a database

Should not have
• We are looking a very minimalistic logo. It should not be an explicit wind turbine a seagal or anything like that. we are looking for abstract, simple and minimalistic image.

```html
<!DOCTYPE html>
<html lang="es">
<head>
<meta charset="utf-8">
<title>ORVIK — Proyectos Renovables</title>
<link rel="stylesheet" href="https://fonts.googleapis.com/css2?family=Marcellus&family=Source+Sans+3:wght@400;600&family=PT+Serif&display=swap">
<style>
  :root{
    --brand-blue:#3b8bd8;
    --text-dark:#4a4a4a;
    --text-mid:#5c5c5c;
    --header-top:#ffffff;
    --header-bottom:#e9e9e9;
    --nav-top:#fbfbfb;
    --nav-bottom:#e4e4e4;
    --nav-active:#c6c6c6;
    --sky-top:#2f5fae;
    --sky-mid:#6f9fd8;
    --cloud:#c9daf0;
    --grass:#5f8d2b;
    --orange:#f39a1e;
    --orange-dark:#e07c0c;
    --footer-bg:#e6e6e6;
    --panel-frame:rgba(140,170,215,.55);
  }
  *{margin:0;padding:0;box-sizing:border-box}
  html,body{width:1200px;height:1051px;overflow:hidden}
  body{position:relative;background:var(--footer-bg);font-family:"Source Sans 3",Arial,sans-serif;color:var(--text-dark)}

  .site-header{position:absolute;left:0;top:0;width:1200px;height:168px;background:linear-gradient(var(--header-top),var(--header-bottom))}
  .brand{position:absolute;left:96px;top:82px;display:flex;align-items:center;gap:22px}
  .brand-dot{width:34px;height:34px;border-radius:50%;background:var(--brand-blue)}
  .brand-name{font-family:"Marcellus",Georgia,serif;font-size:48px;color:var(--brand-blue);letter-spacing:1px;line-height:1}

  .checkout{position:absolute;left:1010px;top:91px;width:164px;height:32px;display:flex;align-items:center}
  .checkout-pill{position:absolute;left:14px;top:2px;width:150px;height:28px;border-radius:14px;background:linear-gradient(#ffc84a,var(--orange-dark));border:1px solid #c96d06}
  .checkout-label{position:absolute;left:40px;top:5px;font-weight:600;font-size:15px;color:#fff}
  .checkout-arrow{position:absolute;right:6px;top:5px;width:22px;height:18px;border-radius:4px;background:#f08a10;color:#fff;font-size:13px;font-weight:600;text-align:center;line-height:18px}
  .checkout svg{position:absolute;left:0;top:-2px}

  .main-nav{position:absolute;left:0;top:168px;width:1200px;height:57px;background:linear-gradient(var(--nav-top),var(--nav-bottom));border-top:1px solid #d6d6d6;border-bottom:1px solid #cfcfcf}
  .main-nav a{position:absolute;top:0;height:56px;line-height:56px;font-size:17px;color:var(--text-mid);text-decoration:none}
  .main-nav a.active{left:213px;width:136px;text-align:center;background:linear-gradient(#e9e9e9,var(--nav-active))}
  .search{position:absolute;left:1011px;top:17px;width:156px;height:28px;border-radius:14px;background:#fff;border:1px solid #cfcfcf;box-shadow:inset 0 1px 3px rgba(0,0,0,.15)}
  .search span{position:absolute;left:22px;top:4px;font-size:14px;color:#a8a8a8}
  .search svg{position:absolute;right:10px;top:7px}

  .hero{position:absolute;left:0;top:225px;width:1200px;height:665px}
  .hero-photo{position:absolute;inset:0;background:
     radial-gradient(ellipse 380px 120px at 180px 470px,var(--cloud),transparent 70%),
     radial-gradient(ellipse 400px 140px at 560px 380px,var(--cloud),transparent 70%),
     linear-gradient(var(--sky-top) 0%,var(--sky-mid) 55%,#9fc0e6 82%,var(--grass) 92%,#3f6b1c 100%)}
  .hero-title{position:absolute;left:0;top:55px;width:632px;height:142px;background:rgba(205,215,235,.35);padding:16px 0 0 51px}
  .hero-title p{font-size:36px;color:#fff;line-height:61px;letter-spacing:.3px}

  .services-panel{position:absolute;left:667px;top:45px;width:483px;height:568px;border-radius:12px;background:var(--panel-frame)}
  .services-card{position:absolute;left:13px;top:11px;width:457px;height:544px;background:linear-gradient(#ffffff,#f0f0f0 60%,#dcdcdc)}
  .services-list{list-style:none;position:absolute;left:26px;top:24px}
  .services-list li{position:relative;height:43px;line-height:43px;padding-left:31px;font-size:16.5px;color:var(--text-mid)}
  .services-list li.plain{padding-left:31px}
  .services-list svg{position:absolute;left:0;top:13px}

  .site-footer{position:absolute;left:0;top:890px;width:1200px;height:161px;background:var(--footer-bg);border-top:3px solid #f2f2f2;font-family:"PT Serif",Georgia,serif;font-size:14.5px;color:#555}
  .footer-links{position:absolute;left:44px;top:24px}
  .footer-copy{position:absolute;left:44px;top:54px}
  .footer-energy{position:absolute;right:76px;top:23px;color:var(--orange-dark)}
  .footer-address{position:absolute;left:818px;top:70px;line-height:29px}
  .footer-mail{position:absolute;left:1070px;top:62px}
</style>
</head>
<body>
  <header class="site-header">
    <div class="brand"><span class="brand-dot"></span><span class="brand-name">ORVIK</span></div>
    <a class="checkout" href="#">
      <svg width="36" height="34" viewBox="0 0 36 34"><path d="M2 6h6l4 16h18l4-12H10" fill="#f5a623" stroke="#5a3a08" stroke-width="2"/><circle cx="14" cy="28" r="3" fill="#333"/><circle cx="27" cy="28" r="3" fill="#333"/><path d="M20 4v9m-4-4 4 4 4-4" stroke="#1a1a1a" stroke-width="2.5" fill="none"/></svg>
      <span class="checkout-pill"></span>
      <span class="checkout-label">Check Out</span>
      <span class="checkout-arrow">»</span>
    </a>
  </header>

  <nav class="main-nav">
    <a style="left:34px" href="#">Lnicio</a>
    <a style="left:111px" href="#">Servicios</a>
    <a class="active" href="#">Productos</a>
    <a style="left:376px" href="#">Nuestra E</a>
    <a style="left:490px" href="#">specialidad</a>
    <a style="left:630px" href="#">Contacto</a>
    <div class="search"><span>Search</span>
      <svg width="15" height="14" viewBox="0 0 15 14"><circle cx="5.5" cy="5.5" r="4" stroke="#888" stroke-width="1.6" fill="none"/><path d="M8.5 8.5l5 4" stroke="#888" stroke-width="2"/></svg>
    </div>
  </nav>

  <section class="hero">
    <div class="hero-photo" role="img" aria-label="Fotografía de aerogeneradores blancos bajo un cielo azul con nubes sobre un campo verde"></div>
    <div class="hero-title">
      <p>PROYECTOS RENOVABLES</p>
      <p>PARA MEXICO Y LATINO AMERICA</p>
    </div>
    <div class="services-panel">
      <div class="services-card">
        <ul class="services-list">
          <li><svg width="17" height="17"><circle cx="8.5" cy="8.5" r="8" fill="var(--orange)"/><path d="M4.5 8.5l3 3 5-6" stroke="#fff" stroke-width="2" fill="none"/></svg>&nbsp;Energia Eolica</li>
          <li><svg width="17" height="17"><circle cx="8.5" cy="8.5" r="8" fill="var(--orange)"/><path d="M4.5 8.5l3 3 5-6" stroke="#fff" stroke-width="2" fill="none"/></svg>Proyectos de Generacion Eolica desde 1MW</li>
          <li class="plain">hasta 200 MV</li>
          <li><svg width="17" height="17"><circle cx="8.5" cy="8.5" r="8" fill="var(--orange)"/><path d="M4.5 8.5l3 3 5-6" stroke="#fff" stroke-width="2" fill="none"/></svg>Analisis Detallado de Recurso Eolico</li>
          <li><svg width="17" height="17"><circle cx="8.5" cy="8.5" r="8" fill="var(--orange)"/><path d="M4.5 8.5l3 3 5-6" stroke="#fff" stroke-width="2" fill="none"/></svg>Diseno de Parques Eolicos</li>
          <li><svg width="17" height="17"><circle cx="8.5" cy="8.5" r="8" fill="var(--orange)"/><path d="M4.5 8.5l3 3 5-6" stroke="#fff" stroke-width="2" fill="none"/></svg>Permitologia</li>
          <li><svg width="17" height="17"><circle cx="8.5" cy="8.5" r="8" fill="var(--orange)"/><path d="M4.5 8.5l3 3 5-6" stroke="#fff" stroke-width="2" fill="none"/></svg>Comision Nacional de Energia Limpia CNEL</li>
          <li><svg width="17" height="17"><circle cx="8.5" cy="8.5" r="8" fill="var(--orange)"/><path d="M4.5 8.5l3 3 5-6" stroke="#fff" stroke-width="2" fill="none"/></svg>SEDAMAR</li>
          <li><svg width="17" height="17"><circle cx="8.5" cy="8.5" r="8" fill="var(--orange)"/><path d="M4.5 8.5l3 3 5-6" stroke="#fff" stroke-width="2" fill="none"/></svg>CRN</li>
          <li><svg width="17" height="17"><circle cx="8.5" cy="8.5" r="8" fill="var(--orange)"/><path d="M4.5 8.5l3 3 5-6" stroke="#fff" stroke-width="2" fill="none"/></svg>Analisis de Riesgo y Factibilidad Financiera</li>
          <li><svg width="17" height="17"><circle cx="8.5" cy="8.5" r="8" fill="var(--orange)"/><path d="M4.5 8.5l3 3 5-6" stroke="#fff" stroke-width="2" fill="none"/></svg>PPA and Tariff Analysis</li>
        </ul>
      </div>
    </div>
  </section>

  <footer class="site-footer">
    <p class="footer-links">Carreras | Quienes Somos</p>
    <p class="footer-copy">Copyright © 2012 www.orvik.com</p>
    <p class="footer-energy">Energia Eolica | Energia Solar</p>
    <address class="footer-address" style="font-style:normal">Jacarandas 212, Col. Valle Alto Sur,<br>Monterrey, N.L. 64790</address>
    <svg class="footer-mail" width="60" height="60" viewBox="0 0 60 60"><g transform="rotate(-18 30 30)"><rect x="6" y="16" width="48" height="32" rx="3" fill="#f2b731" stroke="#c98a12" stroke-width="1.5"/><path d="M6 17l24 18 24-18" fill="none" stroke="#fff3c4" stroke-width="2.5"/></g></svg>
  </footer>
</body>
</html>
```